Raising floral designer needs an artistic business card

I am an award winning floral designer wishing to transition from commercial wedding/event work to show designs as well as educating and consulting the art of flowers. My design style is the fusion of Ikebana and European floral art, so I wish my business card reflects it. I would like my card give people creative and energetic impression combined with the subtlety and gracefulness of the Eastern culture.
Target Market(s)
General public as well as related professionals
Industry/Entity Type
Floral
Contact Information for Business Card
Marla Dovien Holt NGPB, RTA.
Floral Artist and Consultant.
Phone: 417-296-7183.   email: marlapetals@kelvamail.com
Requirements
Must have
- color, floral/plant element, clean-looking
Nice to have
- a set with different color background/designs or shapes.
Should not have
- psychedelic colors and lines, illegible fonts.

```html
<!DOCTYPE html>
<html lang="en">
<head>
<meta charset="utf-8">
<title>Marla Dovien Holt — Floral Artist and Consultant</title>
<link rel="stylesheet" href="https://fonts.googleapis.com/css2?family=Bebas+Neue&family=Parisienne&family=Oswald:wght@300&display=swap">
<style>
  :root {
    --card-dark: #1b2326;
    --card-mid: #232c2c;
    --card-edge: #2a2a2f;
    --bloom-violet: #3b3561;
    --bloom-blue: #302f5a;
    --bloom-green: #2f4033;
    --bloom-rose: #4a3a3c;
    --vase-grey: #3a3e3f;
    --name-lavender: #dcc6f2;
    --line-white: #f4f2f6;
    --script-mint: #e6f3ee;
    --ornament-tint: rgba(244, 242, 246, 0.16);
  }
  html, body {
    margin: 0;
    padding: 0;
    width: 1200px;
    height: 720px;
    overflow: hidden;
    background: var(--card-dark);
  }
  .business-card {
    position: relative;
    width: 1200px;
    height: 720px;
    overflow: hidden;
    background: linear-gradient(100deg, var(--card-dark) 0%, var(--card-mid) 55%, var(--card-edge) 100%);
  }
  .floral-photo {
    position: absolute;
    left: 110px;
    top: 30px;
    width: 1070px;
    height: 690px;
    border-radius: 40px;
    background:
      radial-gradient(ellipse 90px 200px at 330px 600px, var(--vase-grey), transparent 75%),
      radial-gradient(ellipse 260px 120px at 230px 380px, var(--bloom-violet), transparent 75%),
      radial-gradient(ellipse 120px 260px at 250px 200px, var(--bloom-blue), transparent 75%),
      radial-gradient(ellipse 300px 110px at 860px 460px, var(--bloom-blue), transparent 75%),
      radial-gradient(ellipse 200px 120px at 580px 470px, var(--bloom-rose), transparent 75%),
      radial-gradient(ellipse 220px 140px at 640px 640px, var(--bloom-rose), transparent 75%),
      radial-gradient(ellipse 420px 220px at 560px 330px, var(--bloom-green), transparent 75%);
  }
  .frame-lines {
    position: absolute;
    inset: 0;
  }
  .crest-ornament {
    position: absolute;
    left: 443px;
    top: 69px;
    width: 314px;
    height: 102px;
    border-radius: 50px 50px 8px 8px;
    background: radial-gradient(ellipse at center, var(--ornament-tint), transparent 75%);
  }
  .designer-name {
    position: absolute;
    left: 0;
    right: 0;
    top: 258px;
    margin: 0;
    text-align: center;
    font-family: "Bebas Neue", "Oswald", sans-serif;
    font-weight: 400;
    font-size: 80px;
    line-height: 1;
    letter-spacing: 1px;
    color: var(--name-lavender);
  }
  .designer-role {
    position: absolute;
    left: 0;
    right: 0;
    top: 355px;
    margin: 0;
    text-align: center;
    font-family: "Parisienne", cursive;
    font-size: 38px;
    line-height: 1.2;
    color: var(--script-mint);
  }
  .contact-line {
    position: absolute;
    top: 558px;
    margin: 0;
    font-family: "Oswald", sans-serif;
    font-weight: 300;
    font-size: 36px;
    line-height: 1;
    color: var(--line-white);
  }
  .contact-phone { left: 203px; }
  .contact-email { right: 203px; }
</style>
</head>
<body>
  <main class="business-card">
    <div class="floral-photo" role="img" aria-label="Dim photograph of a lupine and wildflower arrangement in a slim metal vase beside seashells"></div>

    <div class="crest-ornament" role="img" aria-label="Decorative scrollwork crest with a central fleur motif"></div>

    <svg class="frame-lines" width="1200" height="720" viewBox="0 0 1200 720" aria-hidden="true">
      <g stroke="var(--line-white)" stroke-width="2" fill="none">
        <line x1="160" y1="176" x2="544" y2="176"/>
        <line x1="656" y1="176" x2="1040" y2="176"/>
        <line x1="203" y1="192" x2="578" y2="192"/>
        <line x1="622" y1="192" x2="997" y2="192"/>
        <path d="M600 182 L611 192 L600 202 L589 192 Z"/>
        <line x1="203" y1="608" x2="578" y2="608"/>
        <line x1="622" y1="608" x2="997" y2="608"/>
        <path d="M600 598 L611 608 L600 618 L589 608 Z"/>
      </g>
      <g fill="var(--line-white)">
        <path d="M149 176 L164 170 L160 176 L164 182 Z"/>
        <path d="M1051 176 L1036 170 L1040 176 L1036 182 Z"/>
      </g>
    </svg>

    <h1 class="designer-name">Marla Dovien Holt NGPB, RTA</h1>
    <p class="designer-role">Floral Artist and Consultant</p>

    <p class="contact-line contact-phone">+417-296-7183</p>
    <p class="contact-line contact-email">marlapetals@kelvamail.com</p>
  </main>
</body>
</html>
```